Webdesign für ELektroinstallationsbetrieb
Zielgruppe
Elektroinstallation für ENergie und Gebäudetechnik
Aufgabenstellung
Ich möchte ein neues modernes Webdesign, alle nötigen Daten kann man der alten Webseite entnehmen. www.strom-haberl-beispiel.de

```html
<!DOCTYPE html>
<html lang="de">
<head>
<meta charset="utf-8">
<title>Haberl Elektrotechnik</title>
<link href="https://fonts.googleapis.com/css2?family=Catamaran:wght@300;400;500;600;700&display=swap" rel="stylesheet">
<style>
:root{
  --green:#8dbd2b;
  --green-dark:#7fae22;
  --slate:#37505a;
  --ink:#4a4a4a;
  --heading:#3b4d55;
  --white:#ffffff;
  --paper:#f7f8f8;
}
*{box-sizing:border-box;margin:0;padding:0}
html,body{width:1200px;height:2625px;overflow:hidden}
body{position:relative;background:var(--white);font-family:"Catamaran",sans-serif;color:var(--ink)}
.top-rule{position:absolute;left:0;top:0;width:1200px;height:3px;background:linear-gradient(90deg,var(--green),#b8c4c8)}
.hero{position:absolute;left:0;top:3px;width:1200px;height:503px;background:linear-gradient(180deg,#fafafa,#f1f3f3);overflow:hidden}
.logo{position:absolute;left:240px;top:22px;display:flex;align-items:center;gap:10px}
.logo-dot{width:40px;height:40px;border-radius:50%;background:var(--green)}
.logo-name{font-size:28px;font-weight:700;color:var(--green);line-height:1}
.hero-photo{position:absolute;left:40px;top:100px;width:455px;height:403px;border-radius:46% 46% 0 0;background:radial-gradient(ellipse at 50% 40%,#9a8f86,#7b8a94 55%,#d9dee0 90%)}
.badge{position:absolute;left:490px;top:76px;width:470px;height:470px;border-radius:50%;background:var(--green);box-shadow:0 10px 30px rgba(0,0,0,.18);text-align:center;color:var(--white)}
.badge-title{margin-top:55px;font-size:23px;font-weight:600;color:var(--slate);line-height:1}
.badge-sub{font-size:18px;font-weight:600;color:var(--slate);margin-top:4px}
.badge-list{list-style:none;margin-top:14px;font-size:13px;font-weight:400;line-height:24.7px}
.badge-quote{width:310px;margin:28px auto 0;border-top:1px solid rgba(255,255,255,.7);border-bottom:1px solid rgba(255,255,255,.7);padding:21px 0;font-size:13px;text-align:left}
.badge-buttons{display:flex;gap:9px;justify-content:center;margin-top:26px}
.btn{display:block;width:151px;height:34px;line-height:34px;background:var(--slate);color:var(--white);font-size:11.5px;text-decoration:none}
.contact-band{position:absolute;left:0;top:506px;width:1200px;height:160px;background:var(--slate);text-align:center;color:var(--white)}
.contact-band h2{margin-top:40px;font-size:23px;font-weight:600;color:var(--green);line-height:1}
.contact-line{margin-top:14px;font-size:14.5px;font-weight:600;display:flex;justify-content:center;align-items:center;gap:6px}
.contact-line a{color:var(--green);text-decoration:none}
.contact-line .sep{margin:0 8px}
.contact-note{font-size:12.5px;font-weight:400;margin-top:4px}
.band-photo{position:absolute;left:950px;top:450px;width:190px;height:216px;border-radius:48% 48% 0 0;background:linear-gradient(180deg,#d9b79a,#8e7d6d 55%,#5c6166)}
.service{position:absolute;left:240px;width:720px;height:212px}
.service .photo{position:absolute;top:0;width:319px;height:212px}
.service .text{position:absolute;width:355px;font-size:12.5px;line-height:21px;font-weight:400}
.service h3{font-size:23px;font-weight:600;color:var(--green);line-height:1;margin-bottom:14px}
.service p+p{margin-top:7px}
.photo-left .photo{left:0}
.photo-left .text{left:360px}
.photo-right .photo{left:401px}
.photo-right .text{left:5px;text-align:right}
.footer-bg{position:absolute;left:0;top:2300px;width:1200px;height:325px;background:linear-gradient(180deg,#ffffff,#f4f5f5)}
.footer-band{position:absolute;left:0;top:2496px;width:1200px;height:69px;background:var(--slate)}
.footer-band h2{position:absolute;left:432px;top:24px;font-size:23px;font-weight:600;color:var(--green);line-height:1}
.footer-bar{position:absolute;left:0;top:2565px;width:1200px;height:60px;background:var(--green)}
.footer-links{position:absolute;right:240px;top:27px;font-size:11.5px;color:var(--white);display:flex;gap:10px;align-items:center}
.footer-links a{color:var(--white);text-decoration:none;display:flex;align-items:center;gap:4px}
.pill{position:absolute;left:130px;width:140px;height:34px;border-radius:17px;background:var(--slate)}
.address-card{position:absolute;left:240px;top:2435px;width:189px;height:190px;background:var(--slate);border-radius:0 90px 0 0;color:var(--white);font-size:11px;line-height:20px;padding:20px 0 0 23px}
.address-card .firm{color:var(--green);font-weight:600}
.address-card .gap{height:7px}
.address-card .row{display:flex;align-items:center;gap:6px}
.address-card a{color:var(--green);text-decoration:none}
</style>
</head>
<body>
<div class="top-rule"></div>

<header class="hero">
  <div class="logo"><span class="logo-dot"></span><span class="logo-name">Haberl</span></div>
  <div class="hero-photo" role="img" aria-label="Foto: Mann mit elektrisch zerzausten Haaren hält Kabel"></div>
  <section class="badge">
    <h1 class="badge-title">HABERL ELEKTRONIK</h1>
    <p class="badge-sub">IHR PARTNER FÜR:</p>
    <ul class="badge-list">
      <li>Elektroinstallation</li>
      <li>Netzwerktechnik</li>
      <li>Telefonanlagen</li>
      <li>Service Photovoltaik</li>
      <li>Solare Datensysteme</li>
    </ul>
    <p class="badge-quote">„ Lassen Sie das lieber von einem Fachmann machen! “</p>
    <div class="badge-buttons">
      <a class="btn" href="#leistungen">Leistungsbereiche</a>
      <a class="btn" href="#kontakt">Kontaktaufnahme</a>
    </div>
  </section>
</header>

<section class="contact-band" id="kontakt">
  <h2>WIR SIND 24 STUNDEN AM TAG FÜR SIE ERREICHBAR</h2>
  <p class="contact-line">
    <svg width="13" height="13" viewBox="0 0 24 24"><path fill="#fff" d="M6.6 10.8a15 15 0 0 0 6.6 6.6l2.2-2.2a1 1 0 0 1 1-.25 11.4 11.4 0 0 0 3.6.57 1 1 0 0 1 1 1V20a1 1 0 0 1-1 1A17 17 0 0 1 3 4a1 1 0 0 1 1-1h3.5a1 1 0 0 1 1 1c0 1.25.2 2.45.57 3.57a1 1 0 0 1-.25 1z"/></svg>
    Telefon +49 8031-555 12 34 <span class="sep">oder</span>
    <svg width="15" height="12" viewBox="0 0 24 18"><rect width="24" height="18" rx="2" fill="#fff"/><path d="M1 2l11 8 11-8" stroke="#37505a" stroke-width="2" fill="none"/></svg>
    E-Mail <a href="#">info@strom-haberl-beispiel.de</a>
  </p>
  <p class="contact-note">Rufen Sie uns an, oder schreiben Sie per Mail. Wir werden Ihnen zeitnah weiter helfen und für Sie da sein.</p>
</section>
<div class="band-photo" role="img" aria-label="Foto: junger Elektriker im karierten Hemd"></div>

<main id="leistungen">
  <article class="service photo-left" style="top:711px">
    <div class="photo" role="img" aria-label="Foto: Elektriker arbeitet am Schaltschrank" style="background:linear-gradient(135deg,#e8ecef,#9aa7b3 60%,#3e63a6)"></div>
    <div class="text">
      <h3>Energie- und Gebäudetechnik</h3>
      <p>Elektrotechnik Haberl, Ihr kompetenter Partner für moderne Elektroinstallation und Elektroplanung in den Bereichen Neubau und Altbaurenovierung.</p>
      <p>Eine ausführliche Beratung, genaue Planung und fachgerechte Installation gehören zu unseren täglichen Aufgaben.<br>Wir sind Ihr Partner vor Ort um jederzeit individuelle und persönlich auf Sie zugeschnittene Lösungen zu finden.</p>
    </div>
  </article>

  <article class="service photo-right" style="top:983px">
    <div class="text">
      <h3>Solare Datensysteme</h3>
      <p>Wir bieten Ihnen modernste Monitoring-Systeme mit umfangreicher und professioneller Auswertungssoftware, die jederzeit per PC, Tablet oder Handy erreichbar ist.</p>
      <p>Das intelligente Monitoring-System sammelt alle Daten Ihrer PV-Anlage, wertet diese aus und informiert Sie mit zahlreichen Zusatzdienstleistungen per Email oder SMS über mögliche Störungen oder drohende Ertragsausfälle.</p>
    </div>
    <div class="photo" role="img" aria-label="Foto: Hände halten Tablet mit Diagramm" style="background:linear-gradient(135deg,#f2f2f0,#c9cdd2 45%,#2a5aa8 75%,#c79a7a)"></div>
  </article>

  <article class="service photo-left" style="top:1255px">
    <div class="photo" role="img" aria-label="Foto: lächelnder Mann am Laptop" style="background:linear-gradient(135deg,#f4f4f2,#e4e4e2 50%,#2e3f52)"></div>
    <div class="text">
      <h3>KNX und SPs Programmierung</h3>
      <p>Über BUS-Systeme lassen sich im Haus viele Steuerungsmöglichkeiten für verschiedene Anwendungen verwirklichen. Die zentrale Steuerung von Lichtern und Rollläden gewinnt immer mehr an Bedeutung.</p>
      <p>Ein BUS-System ist ständig erweiterbar und bietet zahlreiche Funktionen um Energie effizienter einzusetzen und den Komfort zu erhöhen.</p>
    </div>
  </article>

  <article class="service photo-right" style="top:1527px">
    <div class="text" style="top:50px">
      <h3>Satelliten / Antennentechnik</h3>
      <p>Digitale Medien sind heute nicht mehr wegzudenken. Egal ob Sie diese über Satellit, Antenne oder Kabel empfangen, wir beraten Sie professionell und installieren Ihnen Ihre Empfangsanlage auf dem neuesten Stand der Technik.</p>
    </div>
    <div class="photo" role="img" aria-label="Foto: Fußballfans jubeln vor dem Fernseher" style="background:linear-gradient(135deg,#f3f3f3,#e6e6e6 50%,#b98c5f)"></div>
  </article>

  <article class="service photo-left" style="top:1800px">
    <div class="photo" role="img" aria-label="Foto: Geschäftsmann telefoniert im Büro" style="background:linear-gradient(135deg,#c8d8ea,#eef2f6 55%,#2f4f86)"></div>
    <div class="text" style="top:42px">
      <h3>Telefon und ISDN Anlagen</h3>
      <p>Ob analog, ISDN oder moderne DSL-Technik, der Bereich der Telekommunikation steht und stand in den letzten Jahren in einem starken Wandel.</p>
      <p>Was Sie auch benötigen, wir erarbeiten zusammen mit Ihnen maßgeschneiderte Lösungen für Ihre Bedürfnisse.</p>
    </div>
  </article>

  <article class="service photo-right" style="top:2071px">
    <div class="text">
      <h3>Netzwerktechnik</h3>
      <p>Wenn Sie Netzwerktechnik von morgen wollen und keine Lösungen, die heute schon von gestern sind, vertrauen Sie unserer Erfahrung.</p>
      <p>EDV-gestützte Organisations- und Arbeitshilfen sind heute in fast allen Branchen unverzichtbarer Bestandteil erfolgreicher Betriebskonzepte und Voraussetzung für zeitgemäße Bürokommunikation.</p>
    </div>
    <div class="photo" role="img" aria-label="Foto: Techniker mit Laptop im Serverraum" style="background:linear-gradient(135deg,#d9dde2,#8d96a0 50%,#2a3440)"></div>
  </article>
</main>

<footer>
  <div class="footer-bg"></div>
  <div class="pill" style="top:2462px"></div>
  <div class="pill" style="top:2567px"></div>
  <div class="footer-band"><h2>WIR SIND 24 STUNDEN AM TAG FÜR SIE ERREICHBAR</h2></div>
  <div class="footer-bar">
    <nav class="footer-links">
      <a href="#"><svg width="10" height="10" viewBox="0 0 10 10"><rect width="10" height="10" rx="1.5" fill="#fff"/></svg>Netzwerk</a>
      <span>|</span>
      <a href="#"><svg width="11" height="11" viewBox="0 0 24 24"><path fill="#fff" d="M3 21l9-9 2 2-9 9zM13 3l8 8-3 3-8-8z"/></svg>Datenschutz / Impressum</a>
    </nav>
  </div>
  <address class="address-card" style="font-style:normal">
    <div class="firm">Haberl Elektrotechnik</div>
    <div>Markus Haberl</div>
    <div>Lindenstraße 12</div>
    <div>83000 Musterstadt</div>
    <div class="gap"></div>
    <div class="row"><svg width="10" height="10" viewBox="0 0 24 24"><path fill="#fff" d="M6.6 10.8a15 15 0 0 0 6.6 6.6l2.2-2.2a1 1 0 0 1 1-.25 11.4 11.4 0 0 0 3.6.57 1 1 0 0 1 1 1V20a1 1 0 0 1-1 1A17 17 0 0 1 3 4a1 1 0 0 1 1-1h3.5a1 1 0 0 1 1 1c0 1.25.2 2.45.57 3.57a1 1 0 0 1-.25 1z"/></svg>+49 8031-555 12 34</div>
    <div class="row"><svg width="10" height="10" viewBox="0 0 10 10"><rect x="2" y="0" width="6" height="3" fill="#fff"/><rect x="0" y="3.5" width="10" height="6.5" rx="1" fill="#fff"/></svg>+49 8031-555 12 35</div>
    <div class="row"><svg width="11" height="9" viewBox="0 0 24 18"><rect width="24" height="18" rx="2" fill="#fff"/><path d="M1 2l11 8 11-8" stroke="#37505a" stroke-width="2" fill="none"/></svg><a href="#">info@strom-haberl-beispiel.de</a></div>
  </address>
</footer>
</body>
</html>
```